Wexley Malt Keller Beer Bottle Label #1

A beer bottle label is required for WMK's first beer that will go on sale later this year.
It is hoped that an on-going relationship will be formed with the successful designer.
Designs for glasses, packaging, t-shirts etc will also be required later this year.
Designs should reflect the local origin of the brewery and project an image of tradition and quality.
Designs should be simple, clean, classic and classy.
Designs should not be loud, bright, crazy or busy.
Design should include an element that can be used as brewery logo.
'Malt Keller' to be prominent, 'Wexley' to be discreet.
Name of first beer to be Wexil-Dunkel - label shall be easily adapted for different beers e.g. Wexil-Mirbt.
Deliverables include a smaller text only label for back of the bottle.

***I also need a logo that goes with my label design. So whoever submitted a logo that I like will be selected as the 2nd place winner.

Please refer to the attachment on this brief.

Requirements
Must have
• See uploaded design brief.
Nice to have
Should not have

```html
<!DOCTYPE html>
<html lang="en">
<head>
<meta charset="utf-8">
<title>Malt Keller – Wexil-Dunkel Label</title>
<link href="https://fonts.googleapis.com/css2?family=Oswald:wght@300;400&family=Rye&family=Montserrat:wght@400&family=Mulish:wght@300&display=swap" rel="stylesheet">
<style>
  :root {
    --paper: #fcf8f3;
    --ink: #3b3b3b;
    --ink-soft: #6a6a6a;
    --stripe: #d9d6d1;
    --barrel: #ece6dc;
    --barrel-edge: #e4ddd1;
  }
  * { margin: 0; padding: 0; box-sizing: border-box; }
  html, body { width: 1200px; height: 810px; overflow: hidden; background: var(--paper); }
  .label {
    position: relative;
    width: 1200px;
    height: 810px;
    background: var(--paper);
    color: var(--ink);
    font-family: "Oswald", sans-serif;
    overflow: hidden;
  }
  .stripe-band {
    position: absolute;
    left: 0;
    width: 100%;
    height: 36px;
    background: repeating-linear-gradient(90deg, var(--stripe) 0 13px, transparent 13px 24px);
    background-position: 8px 0;
  }
  .stripe-band.top { top: 0; height: 36px; }
  .stripe-band.bottom { bottom: 0; height: 44px; }

  .batch-info {
    position: absolute;
    left: 72px;
    top: 84px;
    font-weight: 400;
    font-size: 17px;
    letter-spacing: 0.5px;
    line-height: 24px;
  }
  .batch-info .bottled { margin-bottom: 28px; }

  .brand-mark {
    position: absolute;
    left: 520px;
    top: 130px;
    width: 140px;
    display: flex;
    flex-direction: column;
    align-items: center;
    gap: 10px;
  }
  .brand-mark .mark-square {
    width: 44px;
    height: 44px;
    background: var(--ink-soft);
  }
  .brand-mark .mark-name {
    font-family: "Oswald", sans-serif;
    font-weight: 400;
    font-size: 17px;
    letter-spacing: 2px;
    color: var(--ink-soft);
  }

  .barrel {
    position: absolute;
    top: 275px;
    height: 322px;
    background: radial-gradient(ellipse at center, var(--barrel) 0%, var(--barrel-edge) 70%, transparent 100%);
    border-radius: 40% 40% 30% 30%;
    opacity: 0.75;
  }
  .barrel.left { left: 172px; width: 275px; }
  .barrel.right { left: 702px; width: 300px; }

  .beer-title {
    position: absolute;
    left: 0;
    width: 1196px;
    top: 372px;
    text-align: center;
    font-family: "Rye", serif;
    font-size: 50px;
    letter-spacing: 1px;
    color: var(--ink);
  }
  .beer-style {
    position: absolute;
    left: 0;
    width: 1196px;
    top: 523px;
    text-align: center;
    font-family: "Montserrat", sans-serif;
    font-size: 19px;
    letter-spacing: 2.5px;
    line-height: 32px;
    color: var(--ink);
  }
  .beer-volume {
    position: absolute;
    left: 0;
    width: 1168px;
    top: 706px;
    text-align: center;
    font-size: 18px;
    letter-spacing: 1px;
  }
  .origin {
    position: absolute;
    left: 914px;
    width: 220px;
    top: 646px;
    text-align: center;
    font-size: 17px;
    letter-spacing: 1.2px;
    line-height: 27px;
  }
  .ingredients {
    position: absolute;
    left: 92px;
    top: 330px;
    height: 356px;
    writing-mode: vertical-rl;
    transform: rotate(180deg);
    font-family: "Mulish", sans-serif;
    font-weight: 300;
    font-size: 12.5px;
    color: var(--ink-soft);
    white-space: nowrap;
  }
  .brewery-address {
    position: absolute;
    left: 1050px;
    top: 108px;
    writing-mode: vertical-rl;
    font-family: "Mulish", sans-serif;
    font-weight: 300;
    font-size: 14px;
    line-height: 21px;
    color: var(--ink-soft);
    white-space: nowrap;
  }
</style>
</head>
<body>
<main class="label">
  <div class="stripe-band top"></div>

  <div class="batch-info">
    <p class="bottled">BOTTLED JUN' 2018</p>
    <p>BEST BEFORE: 12.06.19.</p>
    <p>(KEEP REFRIGERATED)</p>
  </div>

  <div class="brand-mark">
    <span class="mark-square"></span>
    <span class="mark-name">MALT KELLER</span>
  </div>

  <div class="barrel left" role="img" aria-label="Faint engraved illustration of a wooden barrel on a stand"></div>
  <div class="barrel right" role="img" aria-label="Faint engraved illustration of a wooden barrel on a stand"></div>

  <h1 class="beer-title">MALT KELLER'</h1>

  <p class="beer-style">WEXIL-DUNKEL<br>PREMIUM LAGER BEER</p>

  <p class="beer-volume">500ML, ABV 4.6%, 2.3 UNITS</p>

  <p class="origin">MADE IN<br>WEXLEY, ENGLAND.</p>

  <p class="ingredients">Ingredients (Barley. Hops. Water. Yeast)</p>

  <p class="brewery-address">WMK, The Brewery, . WX4 KL2, England<br>High quality beers inspired by tradition and quality</p>

  <div class="stripe-band bottom"></div>
</main>
</body>
</html>
```